A-Stand Directional Sign Design

Objective:
We need a professional graphic design for an A-Stand sign that will guide customers arriving in our parking lot to our office. The design should be visually clear, welcoming, and aligned with our brand identity.
REQUIREMENTS:
Two versions of the design:
- One with an arrow pointing left
- One with an arrow pointing right
(This allows us to place the A-Stand anywhere and flip the graphic as needed.)
DIMENSIONS:
- Viewable Area: 30" x 40"
BRAND ALIGNMENT:
- Colors, fonts, and overall style should match our website: www.skornabel.com
- Clean, modern, and professional look consistent with our aviation/tourism brand
CONTENT:
- Clear directional arrow (left or right depending on version)
- Text: “Office Entrance” or similar concise wording (designers may propose alternatives if they improve clarity)
READABILITY:
- Bold, high-contrast design for visibility from a distance
- Simple layout that avoids clutter
DELIVERABLES:
- Final artwork in print-ready format (PDF preferred)
- Two versions: Arrow Left and Arrow Right
DESIGN GOAL:
Ensure customers can easily find our office upon arrival, while reinforcing skorNABEL’s professional and welcoming brand image.
Target Market(s)
Tourism

```html
<!DOCTYPE html>
<html lang="en">
<head>
<meta charset="utf-8">
<title>skorNABEL A-Stand Directional Signs</title>
<link href="https://fonts.googleapis.com/css2?family=Saira+Condensed:wght@700;800&display=swap" rel="stylesheet">
<style>
  :root {
    --page: #f2f2f2;
    --sign-white: #ffffff;
    --brand-blue: #0766f2;
    --ink: #222222;
    --go-green: #037c02;
    --ghost: #d9d9d9;
  }
  html, body {
    margin: 0;
    width: 1200px;
    height: 942px;
    overflow: hidden;
    background: var(--page);
  }
  .sign-set {
    display: flex;
    justify-content: center;
    align-items: center;
    gap: 40px;
    width: 1200px;
    height: 942px;
  }
  .sign {
    position: relative;
    width: 540px;
    height: 720px;
    background: var(--sign-white);
    overflow: hidden;
    box-shadow: 0 2px 10px rgba(0,0,0,0.12);
    font-family: "Saira Condensed", sans-serif;
  }
  .sign-art {
    position: absolute;
    inset: 0;
  }
  .brand {
    position: absolute;
    top: 58px;
    left: 0;
    right: 0;
    display: flex;
    justify-content: center;
    align-items: center;
    gap: 12px;
  }
  .brand-dot {
    width: 40px;
    height: 40px;
    border-radius: 50%;
    background: var(--brand-blue);
  }
  .brand-name {
    font-weight: 700;
    font-size: 34px;
    letter-spacing: 1px;
    color: var(--brand-blue);
    line-height: 1;
  }
  .headline {
    position: absolute;
    top: 140px;
    left: 0;
    right: 0;
    margin: 0;
    text-align: center;
    font-weight: 800;
    line-height: 0.95;
    text-transform: uppercase;
  }
  .headline-top {
    display: block;
    font-size: 112px;
    color: var(--ink);
  }
  .headline-bottom {
    display: block;
    font-size: 124px;
    color: var(--brand-blue);
    letter-spacing: 1px;
  }
</style>
</head>
<body>
<main class="sign-set">

  <section class="sign sign--left">
    <svg class="sign-art" viewBox="0 0 540 720" aria-hidden="false">
      <rect class="ghost-aircraft" x="20" y="420" width="500" height="130" rx="60" fill="var(--ghost)" opacity="0.35" role="img" aria-label="Faint aircraft silhouette decoration"/>
      <path class="ground-band" d="M0 655 L250 595 L540 615 L540 720 L0 720 Z" fill="var(--brand-blue)"/>
      <circle class="arrow-disc" cx="270" cy="510" r="152" fill="var(--go-green)" stroke="var(--sign-white)" stroke-width="5"/>
      <g transform="translate(270 510) scale(-1 1)">
        <polygon class="arrow" points="-95,-28 18,-28 -14,-70 32,-70 98,0 32,70 -14,70 18,28 -95,28" fill="var(--sign-white)" stroke="var(--sign-white)" stroke-width="12" stroke-linejoin="round"/>
      </g>
    </svg>
    <div class="brand">
      <span class="brand-dot"></span>
      <span class="brand-name">SKORNABEL.COM</span>
    </div>
    <h2 class="headline">
      <span class="headline-top">Office</span>
      <span class="headline-bottom">Entrance</span>
    </h2>
  </section>

  <section class="sign sign--right">
    <svg class="sign-art" viewBox="0 0 540 720" aria-hidden="false">
      <rect class="ghost-aircraft" x="20" y="420" width="500" height="130" rx="60" fill="var(--ghost)" opacity="0.35" role="img" aria-label="Faint aircraft silhouette decoration"/>
      <path class="ground-band" d="M0 655 L250 595 L540 615 L540 720 L0 720 Z" fill="var(--brand-blue)"/>
      <circle class="arrow-disc" cx="270" cy="510" r="152" fill="var(--go-green)" stroke="var(--sign-white)" stroke-width="5"/>
      <g transform="translate(270 510)">
        <polygon class="arrow" points="-95,-28 18,-28 -14,-70 32,-70 98,0 32,70 -14,70 18,28 -95,28" fill="var(--sign-white)" stroke="var(--sign-white)" stroke-width="12" stroke-linejoin="round"/>
      </g>
    </svg>
    <div class="brand">
      <span class="brand-dot"></span>
      <span class="brand-name">SKORNABEL.COM</span>
    </div>
    <h2 class="headline">
      <span class="headline-top">Office</span>
      <span class="headline-bottom">Entrance</span>
    </h2>
  </section>

</main>
</body>
</html>
```